Single Page Production Company Site

Clean. Simple. Minimalist site with one page.

No portfolio, just some text to communicate a general overview of what the company does.

We work for a very select group of clients, creating strong brand personalities online. The site is specifically minimal and not communicating too much about what we do.. we have a variety of capabilities to work with clients and prefer to be broad with just a simple landing page as the point of contact for our brand.
Updates

Christmas holidays are coming up, maybe people need some time away from work with family and friends... We can keep working on this and I will provide feedback as quickly as possible, but I understand if designers have other commitments during the coming days. Thanks for your hard work!

Industry/Entity Type

Design Agency

Coding

Coded - Design and coding required

Number of Pages Required

1 page

Font styles to use
Sans Serif

Requirements
Must have
• Clean, bold text headlines.
Nice to have
• Unsure about any images used in the design, would like to see options with or without.

```html
<!DOCTYPE html>
<html lang="en">
<head>
<meta charset="utf-8">
<title>Cedarline Studio Co.</title>
<link rel="stylesheet" href="https://fonts.googleapis.com/css2?family=Roboto:wght@300;400;500;700;900&display=swap">
<style>
:root{
  --brown:#4a2f26;
  --brown-deep:#3a2620;
  --ink:#222222;
  --text:#3a3a3a;
  --muted:#7a7a7a;
  --light:#f1f1f1;
  --panel:#2c2c2c;
  --contact:#3b3b3b;
  --white:#ffffff;
  --rule:#c9c9c9;
}
*{box-sizing:border-box;margin:0;padding:0}
html,body{width:1200px;height:2752px;overflow:hidden}
body{font-family:'Roboto',Arial,sans-serif;color:var(--text);background:var(--white);position:relative}
section,header,footer{position:absolute;left:0;width:1200px}
.abs{position:absolute}

/* header */
.site-header{top:0;height:79px;border-top:3px solid var(--brown-deep);background:var(--white)}
.brand{left:160px;top:8px;color:var(--text)}
.brand-name{font-size:44px;font-weight:700;letter-spacing:3px;line-height:40px;color:#4b4b4b}
.brand-sub{font-size:14px;letter-spacing:3.2px;line-height:16px;color:#4b4b4b}
.contact-chip{top:18px;display:flex;align-items:center;gap:10px}
.chip-icon{width:38px;height:38px;border-radius:50%;background:var(--ink);display:flex;align-items:center;justify-content:center}
.chip-label{font-size:9px;letter-spacing:1px;color:var(--text);line-height:11px}
.chip-value{font-size:12.5px;font-weight:700;color:var(--ink);line-height:15px}
.chip-value.phone{font-size:16px}
.menu-btn{left:1013px;top:28px}

/* hero */
.hero{top:79px;height:585px;background:linear-gradient(120deg,#5d6470 0%,#9aa2ad 30%,#c9ccd0 55%,#7d7f86 80%,#55585f 100%)}
.hero-title{width:100%;text-align:center;top:250px;font-size:44px;font-weight:700;color:var(--white);letter-spacing:.5px;text-shadow:0 3px 8px rgba(0,0,0,.45)}

/* services */
.services{top:664px;height:556px;background:var(--white)}
.eyebrow{font-size:17px;letter-spacing:3px;color:var(--text);font-weight:400}
.headline{font-weight:900;color:var(--ink);letter-spacing:-1.5px;line-height:1}
.rule-line{height:1px;background:var(--rule)}
.rule-line::after{content:"";position:absolute;right:0;top:0;width:30px;height:1px;background:#555}
.intro{font-size:11px;line-height:16px;color:var(--text)}
.service{width:280px}
.service-icon{width:108px;height:108px;border-radius:50%;border:2px dotted var(--ink);display:flex;align-items:center;justify-content:center}
.service-icon span{width:90px;height:90px;border-radius:50%;background:var(--ink);display:flex;align-items:center;justify-content:center}
.service-icon.brown span{background:var(--brown)}
.service-title{margin-top:28px;font-size:23px;font-weight:700;color:var(--ink);line-height:24px}
.service-sub{font-size:16px;letter-spacing:4px;color:var(--ink);line-height:22px;padding-bottom:8px;position:relative}
.service-sub::after{content:"";position:absolute;left:0;bottom:0;width:18px;height:2px;background:var(--ink)}
.service-text{margin-top:14px;font-size:10px;line-height:15px;color:var(--text);width:270px}

/* team */
.team{top:1220px;height:566px;background:var(--light)}
.centered{width:100%;text-align:center}
.team-eyebrow{letter-spacing:8px}
.team-intro{font-size:11px;line-height:18px;color:var(--text)}
.tabs{left:160px;top:219px;width:882px;height:288px;display:flex}
.tab-list{width:220px;background:var(--brown-deep);list-style:none;padding-top:25px}
.tab-list li{height:61px;margin-bottom:1px;background:#2e1f1a;color:var(--white);font-size:13px;font-weight:500;letter-spacing:.8px;display:flex;align-items:center;padding-left:18px}
.tab-list li.active{background:#1f1f1f}
.tab-panel{flex:1;margin-left:2px;position:relative;background:linear-gradient(90deg,#2a2a2a,#3a3a3a 60%,#2e2e2e);padding:72px 28px 0 28px}
.tab-num{position:absolute;right:22px;top:6px;font-size:64px;font-weight:900;color:rgba(255,255,255,.08)}
.tab-panel h3{font-size:22px;font-weight:500;color:var(--white);letter-spacing:.3px;margin-bottom:10px}
.tab-panel p{font-size:12.5px;line-height:19px;color:#8a8a8a;width:600px}

/* we get you */
.about{top:1786px;height:486px;background:var(--white)}
.about-photo{left:160px;top:84px;width:270px;height:325px;background:linear-gradient(150deg,#2c3c46 0%,#6f7d84 40%,#c7b9ad 70%,#8f5f55 100%)}
.about-body{left:464px;top:180px;width:560px;font-size:13.5px;line-height:18px;color:var(--ink)}
.about-body p{margin-bottom:18px}

/* contact */
.contact{top:2272px;height:422px;background:var(--contact)}
.contact .headline{color:var(--white);letter-spacing:-1px}
.field{height:30px;border-bottom:1px solid #9a9a9a;display:flex;justify-content:space-between;align-items:center;color:#9a9a9a;font-size:12px;letter-spacing:1.5px}
.submit{left:160px;top:302px;width:106px;height:45px;background:var(--brown);border:2px solid #8a6a5e;color:var(--white);font-size:17px;font-weight:500;letter-spacing:2px;display:flex;align-items:center;justify-content:center}

/* footer */
.site-footer{top:2694px;height:58px;background:var(--white)}
.copyright{left:160px;top:22px;font-size:10px;letter-spacing:1px;color:var(--text)}
.social{left:886px;top:12px;display:flex;gap:10px;list-style:none}
.social li{width:33px;height:33px;border-radius:50%;border:1.5px solid var(--ink)}
</style>
</head>
<body>

<header class="site-header">
  <div class="brand abs">
    <div class="brand-name">CEDARLINE</div>
    <div class="brand-sub">STUDIO CO.</div>
  </div>
  <div class="contact-chip abs" style="left:512px">
    <div class="chip-icon">
      <svg width="16" height="12" viewBox="0 0 16 12"><rect x="0.5" y="0.5" width="15" height="11" fill="#fff"/><path d="M1 1l7 6 7-6" fill="none" stroke="#222" stroke-width="1.5"/></svg>
    </div>
    <div><div class="chip-label">EMAIL</div><div class="chip-value">HELLO@CEDARLINESTUDIO.COM</div></div>
  </div>
  <div class="contact-chip abs" style="left:804px">
    <div class="chip-icon">
      <svg width="12" height="18" viewBox="0 0 12 18"><rect x="1" y="1" width="10" height="16" rx="2" fill="none" stroke="#fff" stroke-width="1.6"/><circle cx="6" cy="14" r="1" fill="#fff"/></svg>
    </div>
    <div><div class="chip-label">CALL US TODAY</div><div class="chip-value phone">800-555-0172</div></div>
  </div>
  <svg class="menu-btn abs" width="28" height="22" viewBox="0 0 28 22" aria-label="Menu">
    <g fill="#222"><rect x="0" y="1" width="4" height="4"/><rect x="6" y="1" width="22" height="4"/><rect x="0" y="9" width="4" height="4"/><rect x="6" y="9" width="22" height="4"/><rect x="0" y="17" width="4" height="4"/><rect x="6" y="17" width="22" height="4"/></g>
  </svg>
</header>

<section class="hero" role="img" aria-label="Photo of a business team meeting around a table with laptops">
  <h1 class="hero-title abs">CONCEPT · CREATE · COMPLETE</h1>
</section>

<section class="services">
  <div class="eyebrow abs" style="left:160px;top:83px">SERVICES</div>
  <h2 class="headline abs" style="left:160px;top:106px;font-size:62px">WHAT WE DO</h2>
  <div class="rule-line abs" style="left:552px;top:132px;width:288px"></div>
  <p class="intro abs" style="left:160px;top:168px;width:860px">Integer molestie felis dolor. Nulla hendrerit semper ipsum sed placerat. Nunc lorem arcu, fringilla nec cursus sit amet, auctor elementum orci. Suspendisse pellentesque eros eu ipsum aliquet, et tempus dolor vestibulum. Interdum et malesuada fames ac ante ipsum primis in faucibus.</p>

  <div class="service abs" style="left:160px;top:226px">
    <div class="service-icon brown"><span>
      <svg width="44" height="40" viewBox="0 0 44 40" fill="none" stroke="#fff" stroke-width="1.6"><rect x="3" y="3" width="38" height="26"/><path d="M16 29v6h12v-6M12 35h20"/><rect x="9" y="9" width="10" height="8"/><path d="M23 10h12M23 14h12M9 21h26"/></svg>
    </span></div>
    <div class="service-title">DESIGN</div>
    <div class="service-sub">HAPPENS HERE</div>
    <p class="service-text">We are leading the way in design innovation for modern websites. Clean, functional, intuitive websites for progressive businesses.</p>
  </div>

  <div class="service abs" style="left:462px;top:226px">
    <div class="service-icon"><span>
      <svg width="44" height="44" viewBox="0 0 44 44" fill="none" stroke="#fff" stroke-width="1.6"><path d="M22 4C11 4 4 12 4 21c0 10 8 18 17 18 4 0 5-3 3-6-2-3 0-6 4-6h5c5 0 8-3 8-8C41 11 33 4 22 4z"/><circle cx="13" cy="19" r="3"/><circle cx="19" cy="11" r="3"/><circle cx="29" cy="12" r="3"/></svg>
    </span></div>
    <div class="service-title">ART</div>
    <div class="service-sub">HAPPENS HERE</div>
    <p class="service-text">Building brands through design, we believe that contrast is everything. For industry leaders who set the pace and exceed expectations, we help give the company voice and soul.</p>
  </div>

  <div class="service abs" style="left:765px;top:226px">
    <div class="service-icon"><span>
      <svg width="40" height="46" viewBox="0 0 40 46" fill="none" stroke="#fff" stroke-width="1.6"><path d="M20 3C11 3 5 10 5 18c0 6 4 9 6 13v4h18v-4c2-4 6-7 6-13C35 10 29 3 20 3z"/><path d="M13 39h14M15 43h10M20 35V20M15 15l5 5 5-5"/></svg>
    </span></div>
    <div class="service-title">IDEAS</div>
    <div class="service-sub">HAPPENS HERE</div>
    <p class="service-text">Clients look to us for unique, exceptional solutions to their technology issues. We bring creativity to the table and solve your business' problems with actionable solutions.</p>
  </div>
</section>

<section class="team">
  <div class="eyebrow team-eyebrow centered abs" style="top:63px">ABOUT US</div>
  <h2 class="headline centered abs" style="top:90px;font-size:74px">TEAM</h2>
  <p class="team-intro centered abs" style="top:160px">Cedarline Studio Company focuses on creating extraordinary online experiences for extraordinary clients. We'll work with you to create the<br>perfect online presence for your brand.</p>
  <div class="tabs abs">
    <ul class="tab-list">
      <li class="active">SIZE IS EVERYTHING</li>
      <li>OUR GOAL</li>
      <li>WHO'S MILES?</li>
    </ul>
    <div class="tab-panel" role="img" aria-label="Faint photo of an office team behind the text">
      <div class="tab-num">01</div>
      <h3>SIZE IS EVERYTHING</h3>
      <p>We don't work in a massive corporate office and we don't have a mailroom. Not that there's anything wrong with that, it's just that we like knowing each other's names, and encourage our clients to know ours. Our small staff has an advantage – our group works more efficiently, more cost-effectively and most importantly, flexible to each client's unique needs. We deliver a range of services found at any agency, with the personal service you should expect.</p>
    </div>
  </div>
</section>

<section class="about">
  <div class="about-photo abs" role="img" aria-label="Photo of a smiling woman working on a laptop in a bright cafe"></div>
  <h2 class="headline abs" style="left:464px;top:114px;font-size:48px;letter-spacing:-1px">WE GET YOU</h2>
  <div class="rule-line abs" style="left:771px;top:132px;width:269px"></div>
  <div class="about-body abs">
    <p>Having a website isn't enough. You need to show your customers you understand the socially connected online world we live in.</p>
    <p>We help you create designs that capture the personality of your business and project the image you want your customers to see. Maybe you're a small company looking to sell yourself in the big leagues; maybe you're a big company that wants to look approachable; either way, we can make it happen.</p>
    <p>You'll come across looking professional, unique and strikingly hip all at the same time.</p>
  </div>
</section>

<section class="contact">
  <h2 class="headline abs" style="left:160px;top:58px;font-size:62px">CONTACT US</h2>
  <div class="abs" style="left:881px;top:95px;width:55px;height:1px;background:#9a9a9a"></div>
  <div class="field abs" style="left:160px;top:162px;width:264px"><span>NAME</span>
    <svg width="12" height="12" viewBox="0 0 12 12" fill="#777"><circle cx="6" cy="3.5" r="3"/><path d="M0 12c0-4 3-5 6-5s6 1 6 5z"/></svg></div>
  <div class="field abs" style="left:464px;top:162px;width:268px"><span>EMAIL</span>
    <svg width="14" height="10" viewBox="0 0 14 10" fill="#777"><rect width="14" height="10"/></svg></div>
  <div class="field abs" style="left:773px;top:162px;width:267px"><span>PHONE</span>
    <svg width="9" height="14" viewBox="0 0 9 14" fill="none" stroke="#777" stroke-width="1.4"><rect x="1" y="1" width="7" height="12" rx="1.5"/></svg></div>
  <div class="field abs" style="left:160px;top:243px;width:880px"><span>MESSAGE</span>
    <svg width="12" height="12" viewBox="0 0 12 12" fill="#777"><path d="M0 12l1-4 7-7 3 3-7 7z"/></svg></div>
  <div class="submit abs">SUBMIT</div>
</section>

<footer class="site-footer">
  <div class="copyright abs">©2018-2019. CEDARLINE STUDIO COMPANY.</div>
  <ul class="social abs" aria-label="Social links">
    <li aria-label="Social link one"></li>
    <li aria-label="Social link two"></li>
    <li aria-label="Social link three"></li>
    <li aria-label="Social link four"></li>
  </ul>
</footer>

</body>
</html>
```